Pantry Circle is an online food market place that connects foodies who make or grow great food with

We would like a 1/2 A4 page size flyer in landscape to promote our new business. We would like to encourage new home foodies to sign up for a membership on our website www.pantrycirclenz.co.nz and we would like customers who are looking for great food in their local community to search our website for their closest home foodie and support a neighbour who is growing or producing creative food locally

Target Market(s)

Creative food lovers

Industry/Entity Type

Landscape

Colors
acd037
f78f20
33b8a4

Requirements
Must have
• Food images and look groovy
• Must be easy to read and stand out on a notice board
• Website address www.pantrycirclenz.co.nz
Nice to have
• We wish to use this flyer in multiple locations and wish to put in different contact details prior to printing

```html
<!DOCTYPE html>
<html lang="en">
<head>
<meta charset="utf-8">
<title>Pantry Circle flyer</title>
<link href="https://fonts.googleapis.com/css2?family=Lobster&family=Lato:ital,wght@0,700;1,700&display=swap" rel="stylesheet">
<style>
  :root {
    --brown-dark: #4e2108;
    --brown: #6b300c;
    --brown-warm: #7c3a0f;
    --green: #3cc12f;
    --tan: #c8a266;
    --tan-light: #d8b77d;
    --ink: #3a1a06;
    --white: #ffffff;
  }
  * { margin: 0; padding: 0; box-sizing: border-box; }
  html, body { width: 1200px; height: 875px; overflow: hidden; background: #2b2b2b; }
  .flyer { position: relative; width: 1200px; height: 875px; overflow: hidden; }
  .flyer-shapes { position: absolute; inset: 0; }
  .headline {
    position: absolute; left: 52px; top: 42px;
    font-family: "Lobster", cursive; font-size: 50px; line-height: 70px;
    color: var(--green); text-shadow: 2px 2px 3px rgba(0,0,0,.45);
  }
  .headline-sub {
    display: block; font-family: "Lato", sans-serif; font-style: italic; font-weight: 700;
    font-size: 46px; color: var(--white); line-height: 78px;
  }
  .brand-name {
    position: absolute; left: 935px; top: 185px; width: 200px; text-align: center;
    font-family: "Lato", sans-serif; font-weight: 700; font-size: 38px; line-height: 44px;
    color: var(--brown-dark);
  }
  .benefit {
    position: absolute; font-family: "Lato", sans-serif; font-style: italic; font-weight: 700;
    font-size: 27px; line-height: 38px; color: var(--ink);
  }
  .benefit-seller { left: 487px; top: 360px; }
  .benefit-seller span { display: block; }
  .benefit-seller span:nth-child(2) { padding-left: 38px; }
  .benefit-seller span:nth-child(3) { padding-left: 50px; }
  .benefit-buyer { left: 626px; top: 528px; width: 560px; }
  .more-info {
    position: absolute; right: 38px; top: 742px; text-align: right;
    font-family: "Lato", sans-serif; font-weight: 700; font-size: 27px; color: var(--white);
  }
  .web-address {
    position: absolute; right: 38px; top: 785px;
    font-family: "Lobster", cursive; font-size: 42px; color: var(--green);
  }
</style>
</head>
<body>
<main class="flyer">
  <svg class="flyer-shapes" width="1200" height="875" viewBox="0 0 1200 875">
    <defs>
      <linearGradient id="brown-band" x1="0" y1="0" x2="1" y2="0">
        <stop offset="0" stop-color="#4e2108"/>
        <stop offset=".55" stop-color="#7c3a0f"/>
        <stop offset="1" stop-color="#4e2108"/>
      </linearGradient>
      <radialGradient id="tan-panel" cx=".6" cy=".5" r=".7">
        <stop offset="0" stop-color="#dcbb82"/>
        <stop offset="1" stop-color="#b98f52"/>
      </radialGradient>
      <radialGradient id="tart-tones" cx=".5" cy=".55" r=".55">
        <stop offset="0" stop-color="#e0a030"/>
        <stop offset=".45" stop-color="#c2332e"/>
        <stop offset=".8" stop-color="#d9b98a"/>
        <stop offset="1" stop-color="#5d5a57"/>
      </radialGradient>
    </defs>
    <rect class="band-top" width="1200" height="875" fill="url(#brown-band)"/>
    <path class="corner-swoosh" d="M860 0 H1200 V230 C1150 120 1020 30 860 0 Z" fill="#3cc12f"/>
    <path class="corner-swoosh-line" d="M900 0 C1030 30 1150 110 1200 200" fill="none" stroke="#fff" stroke-width="8"/>
    <path class="panel-tan" d="M0 430 C120 300 300 270 450 282 C700 300 950 370 1200 500 V720 H0 Z" fill="url(#tan-panel)"/>
    <path class="panel-edge-green" d="M0 430 C120 300 300 270 450 282 C700 300 950 370 1200 500" fill="none" stroke="#3cc12f" stroke-width="10"/>
    <path class="panel-edge-white" d="M0 440 C120 312 300 283 450 294 C700 312 950 382 1200 512" fill="none" stroke="#fff" stroke-width="6"/>
    <rect class="band-bottom" y="720" width="1200" height="155" fill="#5a2709"/>
    <circle class="photo-ring-green" cx="294" cy="640" r="322" fill="#3cc12f"/>
    <circle class="photo-ring-white" cx="294" cy="640" r="312" fill="#fff"/>
    <circle class="photo-frame" cx="294" cy="640" r="300" fill="url(#tart-tones)" role="img" aria-label="Photo of a fruit tart topped with berries, mango and kiwi"/>
    <circle class="brand-seal" cx="1035" cy="215" r="112" fill="#d8b77d" stroke="#b98f52" stroke-width="4"/>
    <path class="bullet-seller" d="M468 372 L484 360 L484 384 Z" fill="#fff"/>
    <path class="bullet-seller-accent" d="M476 378 L484 372 L484 384 Z" fill="#3cc12f"/>
    <path class="bullet-buyer" d="M607 540 L623 528 L623 552 Z" fill="#fff"/>
    <path class="bullet-buyer-accent" d="M615 546 L623 540 L623 552 Z" fill="#3cc12f"/>
  </svg>

  <h1 class="headline">Be part of our exciting new online food<br>marketplace connecting foodies
    <span class="headline-sub">in your local community</span></h1>

  <div class="brand-name">Pantry<br>Circle</div>

  <p class="benefit benefit-seller">
    <span>As a foodie you can sell your</span>
    <span>home produced or home grown</span>
    <span>produce on our marketplace website</span>
  </p>
  <p class="benefit benefit-buyer">As a food lover you can purchase lovingly grown or prepared food and support your local foodie community while keeping your food miles low</p>

  <p class="more-info">For more information go to:</p>
  <p class="web-address">www.pantrycirclenz.co.nz</p>
</main>
</body>
</html>
```